PDBA website design

We need a page template website design for a cms website. Please see the brief attached for the details.
The client is the Pacific Downhorn Breeders Association which is an organisation promoting the Downhorn Sheep Breed within Australia.

Reason: So that my top few designs can make changes and re-submit.

Target Market(s)

See attached brief

```html
<!DOCTYPE html>
<html lang="en">
<head>
<meta charset="utf-8">
<title>Pacific Downhorn Breeders Association</title>
<link href="https://fonts.googleapis.com/css2?family=Ubuntu:wght@300;400;500;700&family=Lora:ital@1&family=Open+Sans:wght@400;600&display=swap" rel="stylesheet">
<style>
:root{
  --green:#13892f;
  --green-dark:#0b6b22;
  --green-deep:#0a5a1c;
  --yellow:#ffd21a;
  --orange:#f7a600;
  --grass:#5e9a2e;
  --panel:#f1f1f1;
  --text:#444;
  --white:#fff;
}
*{margin:0;padding:0;box-sizing:border-box}
html,body{width:1120px;height:1200px;overflow:hidden}
body{position:relative;font-family:"Open Sans",sans-serif;color:var(--text);
  background:linear-gradient(180deg,#cfe3ee 0,#a9c9d7 200px,#7fae4a 300px,var(--grass) 500px,#4e8a22 1200px)}
.abs{position:absolute}
.topbar{left:0;top:0;width:1120px;height:60px;background:var(--green);border-bottom:4px solid var(--yellow)}
.util{left:708px;top:0;width:250px;height:22px;background:var(--green-deep);border-radius:0 0 10px 10px;
  font:500 11px "Ubuntu",sans-serif;color:var(--white);display:flex;align-items:center;justify-content:center;gap:8px}
.nav{left:356px;top:36px;display:flex;font:500 13px "Ubuntu",sans-serif;color:var(--yellow)}
.nav span{position:absolute;white-space:nowrap;top:0}
.nav .home{background:#eee;color:#333;padding:2px 9px;border-radius:2px;top:-1px}
.drop{left:454px;top:64px;width:80px;background:var(--yellow);font:500 11px "Ubuntu",sans-serif;color:#7a5a00}
.drop div{height:27px;line-height:27px;padding-left:10px;border-bottom:1px solid #f0c000}
.hero{left:160px;top:64px;width:800px;height:374px;background:linear-gradient(180deg,#b9b7b0 0,#a4a39c 150px,#9f8a6a 230px,#7d7c44 300px,#5d7330 374px)}
.dots{left:892px;top:412px;display:flex;gap:8px}
.dots i{width:9px;height:9px;border-radius:50%;background:#ccc}
.dots i:first-child{background:#e02020}
.brandpanel{left:160px;top:4px;width:182px;height:236px;background:linear-gradient(180deg,#fff 0,#fff 150px,rgba(255,255,255,0) 236px)}
.brand{left:176px;top:30px;display:flex;align-items:center;gap:8px;font:700 26px "Ubuntu",sans-serif;color:var(--green)}
.brand i{width:34px;height:34px;border-radius:50%;background:var(--green);display:block}
.tagline{left:170px;top:116px;width:162px;text-align:center;font:italic 12.5px/20px "Lora",serif;color:#333}
.welcome{left:160px;top:438px;width:800px;height:240px;background:var(--panel);box-shadow:0 2px 6px rgba(0,0,0,.3)}
.welcome h1{position:absolute;left:12px;top:16px;font:400 21px "Ubuntu",sans-serif;color:#333}
.welcome h1 b{font-weight:500;color:var(--green)}
.rule{left:12px;top:48px;width:530px;border-top:1px dashed #ccc}
.video{left:10px;top:62px;width:200px;height:142px;background:#fff;border:1px solid #ddd;padding:3px}
.video .shot{width:100%;height:118px;background:linear-gradient(180deg,#c7d8e8,#e5e3df 50%,#cfc8bb)}
.video .bar{height:16px;background:#111;display:flex;align-items:center;gap:6px;padding:0 6px;font:600 7px "Open Sans",sans-serif;color:#fff}
.video .track{flex:1;height:4px;background:#444;border-radius:2px}
.play{left:92px;top:118px;width:26px;height:26px;border-radius:50%;background:rgba(80,80,80,.6)}
.copy{left:220px;top:60px;width:326px;font:300 10.6px/17.6px "Ubuntu",sans-serif;color:#444}
.more{font:600 9.5px "Open Sans",sans-serif;color:var(--green);text-decoration:underline}
.vline{left:558px;top:30px;height:190px;border-left:1px solid #ccc}
.cta{left:572px;width:212px;height:33px;background:linear-gradient(180deg,#ffd236,var(--orange));border-radius:3px;
  font:500 16px/33px "Ubuntu",sans-serif;color:var(--white);padding-left:48px;text-shadow:0 1px 1px rgba(0,0,0,.3)}
.badge{left:572px;width:44px;height:48px}
.box{top:689px;height:149px;background:var(--panel);border-radius:4px}
.box h2{height:34px;background:var(--green-dark);border-bottom:4px solid var(--green);border-radius:4px 4px 0 0;
  font:500 17px/32px "Ubuntu",sans-serif;color:var(--yellow);padding-left:12px}
.box .sub{font:600 10px "Open Sans",sans-serif;color:#555;margin:7px 0 0 8px}
.studs{display:grid;grid-template-columns:90px 93px 70px;margin:8px 0 0 6px;font-size:10px;line-height:14px;color:#666}
.studs span::before{content:"▪ ";color:var(--orange);font-size:8px}
.cal{width:100%;margin-top:4px;font:500 10.5px "Ubuntu",sans-serif;color:var(--green-dark);border-collapse:collapse}
.cal th{text-align:left;color:var(--orange);font-weight:500;font-size:10px;height:18px}
.cal td{height:24px}
.cal th:first-child,.cal td:first-child{padding-left:12px}
.boxmore{right:12px;bottom:8px}
.arrows{right:8px;top:7px;color:var(--yellow);font:700 16px "Ubuntu",sans-serif}
.ad{top:48px;width:110px;height:88px;border:2px solid #ccc}
.tile{top:859px;width:175px;height:119px;border-radius:4px;background:linear-gradient(180deg,#c9d3cc,#b6aea0 55%,#8b8677)}
.tile span{position:absolute;bottom:0;left:0;right:0;height:20px;background:rgba(40,40,40,.55);text-align:center;
  font:500 13px/20px "Ubuntu",sans-serif;color:var(--white)}
.showmore{left:520px;top:987px;width:80px;height:17px;background:var(--orange);font:500 10px/17px "Ubuntu",sans-serif;color:var(--white);text-align:center}
.footer{left:160px;top:1006px;width:800px;height:150px;background:var(--white);border-top:1px solid #ddd}
.footer h3{position:absolute;top:10px;font:400 14px "Ubuntu",sans-serif;color:var(--green)}
.flinks{font:500 10.5px/17px "Ubuntu",sans-serif;color:#555}
.contact{font:400 10px "Open Sans",sans-serif;color:#666}
.contact div{display:flex;gap:8px;align-items:flex-start;height:23px}
.sponsor{left:349px;top:45px;width:114px;height:86px;background:#000;border:3px solid var(--green-dark);
  display:flex;align-items:center;justify-content:center;font:500 13px "Ubuntu",sans-serif;color:var(--white)}
.email{left:494px;top:76px;width:168px;height:23px;border:1px solid #ccc;font:400 10px/21px "Open Sans",sans-serif;color:#777;padding-left:10px}
.subscribe{left:494px;top:107px;width:96px;height:24px;background:linear-gradient(180deg,#ffd236,var(--orange));border-radius:3px;
  font:500 11px/24px "Ubuntu",sans-serif;color:var(--white);text-align:center}
.fsep{top:36px;height:100px;border-left:1px solid #e2e2e2}
.fmark{left:700px;top:32px;width:72px;height:80px;display:flex;align-items:center;justify-content:center;
  font:700 18px "Ubuntu",sans-serif;color:var(--green)}
.bottombar{left:160px;top:1156px;width:800px;height:30px;background:linear-gradient(180deg,var(--yellow),var(--orange));
  font:400 12px/30px "Ubuntu",sans-serif;color:#333;padding-left:6px}
.social{right:12px;top:8px;display:flex;gap:14px}
.social i{width:14px;height:14px;border-radius:50%;background:#333;display:block}
</style>
</head>
<body>

<div class="abs topbar"></div>
<div class="abs util"><span>Members Resources</span><span>|</span><span>WebManager Login</span></div>
<nav class="abs nav">
  <span class="home" style="left:0">Home</span>
  <span style="left:62px">About ▾</span>
  <span style="left:118px">Search</span>
  <span style="left:186px">Member Services</span>
  <span style="left:307px">Stud Pages</span>
  <span style="left:394px">News</span>
  <span style="left:446px">Sales</span>
  <span style="left:498px">Link</span>
  <span style="left:551px">Contact</span>
</nav>

<div class="abs hero" role="img" aria-label="Photograph of a flock of white sheep standing in a green paddock beneath grey hills"></div>
<div class="abs dots"><i></i><i></i><i></i></div>
<div class="abs drop"><div>Member</div><div>Stud</div></div>

<div class="abs brandpanel"></div>
<div class="abs brand"><i></i>PDBA</div>
<p class="abs tagline">The Downhorn is proving to be the ideal prime lamb terminal sire in wide-ranging areas and environments of Australia.</p>

<section class="abs welcome">
  <h1>Welcome to <b>Pacific Downhorn</b></h1>
  <div class="abs rule"></div>
  <div class="abs video">
    <div class="shot" role="img" aria-label="Video still of white sheep"></div>
    <div class="bar"><span>▶</span><span>04:59</span><span class="track"></span><span>10:35</span></div>
  </div>
  <svg class="abs play" viewBox="0 0 26 26"><polygon points="10,7 20,13 10,19" fill="#fff"/></svg>
  <p class="abs copy">Lorem ipsum dolor sit amet, consectetuer adipiscing elit, sed diam nonummy nibh euismod tincidunt ut laoreet dolore magna aliquam erat volutpat. Ut wisi enim ad minim veniam, quis nostrud exerci tation ullamcorper suscipit lobortis nisl ut aliquip ex ea commodo consequat. Duis autem vel eum iriure dolor in hendrerit in vulputate velit esse luptatum zzril delenit augue duis dolore te feugait nulla facilisi ullamcorper suscipit lobortis nisl ut aliquip ex ea commodo consequat.</p>
  <span class="abs more" style="left:478px;top:204px">Read More &gt;&gt;</span>
  <div class="abs vline"></div>

  <div class="abs cta" style="top:27px">Prime Lamb Helpline</div>
  <svg class="abs badge" style="top:20px" viewBox="0 0 44 48"><path d="M22 1 42 8v18c0 12-10 19-20 21C12 45 2 38 2 26V8z" fill="var(--green)" stroke="var(--yellow)" stroke-width="2"/><circle cx="22" cy="24" r="11" fill="none" stroke="#fff" stroke-width="2"/><path d="M18 18c-2 3 2 10 8 12l2-2-3-3-2 1c-2-1-3-3-3-5l1-2-2-3z" fill="#fff"/></svg>

  <div class="abs cta" style="top:100px">Upcoming Events</div>
  <svg class="abs badge" style="top:92px" viewBox="0 0 44 48"><path d="M22 1 42 8v18c0 12-10 19-20 21C12 45 2 38 2 26V8z" fill="var(--green)" stroke="var(--yellow)" stroke-width="2"/><rect x="12" y="14" width="20" height="18" fill="none" stroke="#fff" stroke-width="2"/><path d="M12 19h20M17 19v13M22 19v13M27 19v13M12 25h20" stroke="#fff" stroke-width="1.5"/></svg>

  <div class="abs cta" style="top:171px">Latest News</div>
  <svg class="abs badge" style="top:163px" viewBox="0 0 44 48"><path d="M22 1 42 8v18c0 12-10 19-20 21C12 45 2 38 2 26V8z" fill="var(--green)" stroke="var(--yellow)" stroke-width="2"/><circle cx="22" cy="14" r="4" fill="#fff"/><path d="M10 20h10v14H10zM24 20h10v14H24z" fill="none" stroke="#fff" stroke-width="2"/></svg>
</section>

<section class="abs box" style="left:172px;width:248px">
  <h2>Semen For Sale</h2>
  <p class="sub">From Registered Downhorn Stud Breeders</p>
  <div class="studs">
    <span>Kellaby</span><span>Redmount</span><span>Orbost</span>
    <span>Tarrin Downs</span><span>Velma Grove</span><span>Hilltrack</span>
    <span>Mirrabee</span><span>Foxley Heights</span><span>Calburn</span>
    <span>Tannamore</span><span>Elmwood</span>
  </div>
  <span class="abs more boxmore" style="color:#333">More &gt;&gt;</span>
</section>

<section class="abs box" style="left:437px;width:248px">
  <h2>Sale Calendar</h2>
  <table class="cal">
    <tr><th>Sale</th><th>Sale Start Date</th><th>State</th></tr>
    <tr><td>Marlow Stud</td><td>01/01/2014</td><td>NSW/ACT</td></tr>
    <tr><td>Brenton</td><td>10/10/2014</td><td>SA</td></tr>
    <tr><td>Willara Park</td><td>25/08/14</td><td>SA</td></tr>
  </table>
  <span class="abs more boxmore" style="color:#333">More &gt;&gt;</span>
</section>

<section class="abs box" style="left:702px;width:246px">
  <h2>Members Advertisements</h2>
  <span class="abs arrows">‹ ›</span>
  <div class="abs ad" style="left:8px;background:linear-gradient(180deg,#fff 0,#fff 20%,#8b2d18 20%,#8b2d18 85%,#fff 85%)" role="img" aria-label="Member advertisement for a heifer charity auction"></div>
  <div class="abs ad" style="left:128px;background:linear-gradient(180deg,#8a7a6a,#b8a98e 60%,#a63a1e 88%)" role="img" aria-label="Member advertisement for a national show and sale"></div>
</section>

<div class="abs tile" style="left:174px" role="img" aria-label="Photograph of white sheep"><span>LOREM IPSUM</span></div>
<div class="abs tile" style="left:372px" role="img" aria-label="Photograph of white sheep"><span>LOREM IPSUM</span></div>
<div class="abs tile" style="left:574px" role="img" aria-label="Photograph of white sheep"><span>LOREM IPSUM</span></div>
<div class="abs tile" style="left:772px" role="img" aria-label="Photograph of a white sheep"><span>LOREM IPSUM</span></div>

<div class="abs showmore">▾ Show More</div>

<footer class="abs footer">
  <h3 style="left:13px">Quick Links</h3>
  <div class="abs flinks" style="left:16px;top:40px">Home<br>About<br>Search<br>Member<br>Services<br>Stud Pages</div>
  <div class="abs flinks" style="left:90px;top:41px">News<br>Sales<br>Link<br>Contact Us</div>
  <div class="abs fsep" style="left:163px"></div>

  <h3 style="left:179px">Contact Us</h3>
  <div class="abs contact" style="left:180px;top:43px">
    <div style="height:33px"><svg width="12" height="14" viewBox="0 0 12 14"><path d="M6 0a5 5 0 0 1 5 5c0 4-5 9-5 9S1 9 1 5a5 5 0 0 1 5-5z" fill="#555"/><circle cx="6" cy="5" r="2" fill="#fff"/></svg><span>PO Box 214, Kingsford,<br>SA 5091</span></div>
    <div><svg width="12" height="12" viewBox="0 0 12 12"><path d="M2 1l3 0 1 3-2 1c1 2 2 3 3 3l1-2 3 1v3c-6 0-9-4-9-9z" fill="#555"/></svg><span>(08) 8000 4120</span></div>
    <div><svg width="12" height="12" viewBox="0 0 12 12"><rect x="0" y="4" width="12" height="6" fill="#555"/><rect x="3" y="1" width="6" height="3" fill="#555"/></svg><span>(08) 8000 4121</span></div>
    <div><svg width="12" height="10" viewBox="0 0 12 10"><rect width="12" height="9" fill="#555"/><path d="M0 0l6 5 6-5" stroke="#fff" fill="none"/></svg><span>info@pdba-mail.org</span></div>
  </div>
  <div class="abs fsep" style="left:334px"></div>

  <h3 style="left:349px">Sponsors</h3>
  <div class="abs sponsor">Southgate Bank</div>
  <div class="abs fsep" style="left:477px"></div>

  <h3 style="left:494px">Sign Up to Our Newsletter</h3>
  <p class="abs contact" style="left:494px;top:44px;line-height:14px">Get the latest updates by<br>entering your email address</p>
  <div class="abs email">Enter Your Email ID</div>
  <div class="abs subscribe">SUBSCRIBE</div>
  <div class="abs fsep" style="left:686px"></div>
  <div class="abs fmark">PDBA</div>
</footer>

<div class="abs bottombar">© 2014 pdba. All right reserved.
  <div class="abs social" aria-label="Social links"><i></i><i></i><i></i><i></i></div>
</div>

</body>
</html>
```